new recycling company is looking for more vendors

Ridgeline Cove Recycling is a company that actively purchases surplus and obsolete equipment from various sources; hospitals, manufacturers, logistics companies... We are looking for a full page flyer that we can send to our prospective vendors to inform them about what services we provide. We would like to use the colors similar to our website here: http://marbrookrecyc.example/index.html and include the logo we have there. The attachment is just the back of an old postcard because we want to include just the list of things "we buy", not the contact info because it changed. We'd like to have the words "Reliable Convenient Secure" somewhere.

Target Market(s)

Companies with old equipment, obsolete inventories, scrap and surplus.

Industry/Entity Type

Recycling

Requirements
Must have
• I would focus more on images than text. Text should be brief, images would be great.

We want to make sure they know we buy machinery, test equipment, surplus parts and components.

Images of that type of stuff is preferred over images of computers or wire etc.

```html
<!DOCTYPE html>
<html lang="en">
<head>
<meta charset="utf-8">
<title>Ridgeline Cove Recycling – We Buy Surplus and Obsolete Equipment</title>
<link rel="stylesheet" href="https://fonts.googleapis.com/css2?family=Source+Sans+3:wght@600;700;800&display=swap">
<style>
  :root {
    --black: #0b0b0b;
    --charcoal: #2b2b2b;
    --grey: #6d6d6d;
    --green: #1e6b3c;
    --green-light: #4fae72;
    --white: #ffffff;
    --ink: #111111;
    --devices: #d9d9d6;
  }
  * { margin: 0; padding: 0; box-sizing: border-box; }
  html, body { width: 927px; height: 1200px; overflow: hidden; background: var(--black); }
  .flyer {
    position: relative; width: 927px; height: 1200px; overflow: hidden;
    font-family: "Source Sans 3", "Myriad Pro", Arial, sans-serif;
    background: var(--black);
  }
  .backdrop { position: absolute; inset: 0; }
  .brand {
    position: absolute; left: 18px; top: 30px;
    display: flex; align-items: center; gap: 10px;
    color: var(--white); font-weight: 700; font-size: 17px; line-height: 1.1;
  }
  .brand__dot { width: 22px; height: 22px; border-radius: 50%; background: var(--green); border: 3px solid var(--white); }
  .brand__name { width: 120px; }
  .headline {
    position: absolute; left: 0; top: 178px; width: 455px;
    text-align: center; color: var(--green);
    font-weight: 800; font-size: 57px; line-height: 75px; letter-spacing: -0.3px;
  }
  .buy-list {
    position: absolute; left: 40px; top: 494px; width: 470px;
    text-align: center; color: var(--white); font-weight: 700;
  }
  .buy-list__intro { font-size: 23px; margin-bottom: 26px; margin-left: -30px; }
  .buy-list ul { list-style: none; font-size: 23px; line-height: 31px; }
  .services {
    position: absolute; left: 64px; top: 872px; color: var(--ink); font-weight: 700;
  }
  .services__intro { font-size: 17px; margin-bottom: 16px; }
  .services ul { list-style: none; font-size: 16.5px; line-height: 19.8px; }
  .tagline {
    position: absolute; left: 0; right: 0; top: 1088px;
    text-align: center; padding-left: 70px;
    color: var(--green-light); font-weight: 800; font-size: 22px;
    letter-spacing: 4px; text-transform: uppercase;
  }
  .tagline span + span::before { content: "•"; margin: 0 14px; color: var(--white); }
  .contact {
    position: absolute; left: 0; right: 0; top: 1139px;
    text-align: center; padding-left: 70px;
    color: var(--white); font-weight: 700; font-size: 17px; letter-spacing: 0.1px;
  }
</style>
</head>
<body>
<main class="flyer">
  <svg class="backdrop" width="927" height="1200" viewBox="0 0 927 1200" aria-hidden="true">
    <defs>
      <linearGradient id="steel" x1="0" y1="0" x2="1" y2="1">
        <stop offset="0" stop-color="#4a4a4a"/>
        <stop offset="1" stop-color="#9a9a9a"/>
      </linearGradient>
      <linearGradient id="steel-low" x1="0" y1="0" x2="1" y2="0">
        <stop offset="0" stop-color="#1a1a1a"/>
        <stop offset="1" stop-color="#5c5c5c"/>
      </linearGradient>
      <linearGradient id="cables-tone" x1="0" y1="0" x2="1" y2="1">
        <stop offset="0" stop-color="#8f8a80"/>
        <stop offset="1" stop-color="#c9c4b8"/>
      </linearGradient>
      <linearGradient id="shelves-tone" x1="0" y1="0" x2="1" y2="1">
        <stop offset="0" stop-color="#6f6a60"/>
        <stop offset="1" stop-color="#a39c8e"/>
      </linearGradient>
    </defs>
    <path d="M360 0 H927 V118 C760 118 560 122 430 128 Z" fill="url(#steel)"/>
    <rect x="453" y="18" width="24" height="24" rx="3" fill="var(--green)"/>
    <rect x="490" y="18" width="24" height="24" rx="3" fill="var(--green)"/>
    <rect x="527" y="18" width="24" height="24" rx="3" fill="var(--green)"/>
    <path d="M0 165 C140 150 300 132 440 125 L440 480 L0 480 Z" fill="var(--white)"/>
    <path role="img" aria-label="Photo of tangled cables, keyboards and computer mice" d="M432 122 C600 114 780 112 927 112 V455 H448 C440 340 436 230 432 122 Z" fill="url(#cables-tone)"/>
    <path d="M0 476 C180 470 360 462 523 455 V742 H655 C540 790 330 845 0 845 Z" fill="var(--green)"/>
    <rect role="img" aria-label="Photo of old monitors, printers and computers" x="523" y="455" width="404" height="287" fill="var(--devices)"/>
    <path d="M0 845 C330 845 540 790 655 742 V1000 C420 1030 200 1055 0 1070 Z" fill="var(--white)"/>
    <rect role="img" aria-label="Photo of shelves stacked with vintage test equipment" x="655" y="742" width="272" height="260" fill="url(#shelves-tone)"/>
    <path d="M0 1070 C300 1045 620 1010 927 968 V1200 H0 Z" fill="var(--black)"/>
    <path d="M560 1060 C700 1030 820 1005 927 985 V1040 C840 1050 720 1060 560 1060 Z" fill="url(#steel-low)"/>
  </svg>

  <div class="brand">
    <span class="brand__dot"></span>
    <span class="brand__name">Ridgeline Cove Recycling</span>
  </div>

  <h1 class="headline">We Buy<br>Surplus<br>and Obsolete<br>Equipment.</h1>

  <section class="buy-list">
    <p class="buy-list__intro">Specializing in the purchase of:</p>
    <ul>
      <li>Electronic Assets</li>
      <li>Exccess Inventory</li>
      <li>New &amp; used component parts</li>
      <li>Production Equipment</li>
      <li>Obsolete Electronics</li>
      <li>Computers</li>
      <li>Pallet Racking</li>
      <li>Obsolete Test Equipment</li>
    </ul>
  </section>

  <section class="services">
    <p class="services__intro">We Provide:</p>
    <ul>
      <li>On-site bids in the El Paso and Juarez area</li>
      <li>Speedy local pick-up</li>
      <li>On-site disassembly of equipment and assets</li>
      <li>Certificate of destruction</li>
      <li>Prompt Payment</li>
      <li>Roll-off container and trailer services</li>
    </ul>
  </section>

  <p class="tagline"><span>Reliable</span><span>Convenient</span><span>Secure</span></p>

  <footer class="contact">1480 Calle Verano • El Paso Texas, 79905 • 915.555.0142 • info@marbrookrecyc.example</footer>
</main>
</body>
</html>
```